SEO wiki for a know-how website (rankvale.ch)

Hi,

i need a know-how wiki for an SEO website that looks similar to:

http://demo.plinkora.com/#knowhow

With following know-how categories instead of "account settings" and "API questions":
- Content SEO
- Technical SEO
- Link building
- Influencer marketing
- paid marketing
- analytics & measurement

So i Need the following pages:
1. Landing page with the categories, the search bar and the side-bar
- Sidebar has latest articles, popular articles and categories (in this order)
- On top a nice logo
- on top right -> blog, contact
- on top right below -> social media buttons: brivella, chirpnet

2. a blog site with
- headline
- sub-headline
- date, name
- rating with 5 "know-how" stars
- picture
- article
- info about the author
- related articles
- integration of comment plugin TALVEO

Target Market(s)

SEO folks

Industry/Entity Type

Seo

Logo Text

Do-it yourself SEO

Number of Pages Required

2 page

Font styles to use
Sans Serif

Colors

Designer to choose colors to be used in the design.

```html
<!DOCTYPE html>
<html lang="en">
<head>
<meta charset="utf-8">
<title>rankvale.ch – Know-how</title>
<link href="https://fonts.googleapis.com/css2?family=Varela+Round&display=swap" rel="stylesheet">
<style>
  :root {
    --navy: #33495f;
    --coral: #f98065;
    --text: #4d5560;
    --muted: #7b828a;
    --line: #e6e6e6;
    --footer-bg: #f0f0f0;
    --white: #ffffff;
  }
  * { box-sizing: border-box; margin: 0; padding: 0; }
  html, body { width: 1200px; height: 1187px; overflow: hidden; }
  body {
    font-family: "Varela Round", Arial, sans-serif;
    color: var(--text);
    background: var(--white);
    position: relative;
  }
  a { color: inherit; text-decoration: none; }
  ul { list-style: none; }

  /* Header */
  .site-header { position: relative; height: 87px; }
  .brand { position: absolute; left: 109px; top: 22px; display: flex; align-items: center; gap: 8px; }
  .brand-mark { width: 43px; height: 43px; border-radius: 50%; background: var(--coral); }
  .brand-name { font-size: 29px; line-height: 28px; color: var(--navy); }
  .brand-tagline { font-size: 13.5px; color: var(--muted); margin-top: 2px; }
  .top-nav { position: absolute; right: 111px; top: 14px; display: flex; gap: 17px; font-size: 13.5px; color: var(--muted); }
  .social { position: absolute; right: 111px; top: 40px; display: flex; gap: 6px; }
  .social-btn { width: 29px; height: 29px; border-radius: 50%; border: 2px solid #b9b9b9; display: block; }

  /* Search band */
  .search-band { height: 106px; background: var(--navy); position: relative; }
  .search-form {
    position: absolute; left: 297px; top: 30px; width: 606px; height: 46px;
    background: var(--white); border-radius: 23px; display: flex; align-items: center;
  }
  .search-input { flex: 1; padding-left: 24px; font-size: 13px; color: #8a8f96; }
  .search-btn {
    width: 111px; height: 40px; margin-right: 3px; border-radius: 20px;
    background: var(--coral); color: var(--white); font-size: 13.5px; letter-spacing: .5px;
    display: flex; align-items: center; justify-content: center; gap: 9px;
  }

  /* Main */
  .content { position: absolute; left: 111px; top: 241px; width: 700px; }
  .section-title { font-size: 21px; color: var(--navy); font-weight: normal; }
  .category-grid { display: grid; grid-template-columns: 360px 360px; grid-auto-rows: 272px; margin-top: 24px; }
  .category-head { display: flex; align-items: center; gap: 12px; height: 22px; }
  .category-head h3 { font-size: 16.5px; font-weight: normal; color: var(--navy); }
  .category-head .count { font-size: 12px; color: var(--muted); margin-left: 3px; }
  .article-list { margin-top: 17px; padding-left: 34px; }
  .article-list li { display: flex; gap: 8px; font-size: 13px; line-height: 19px; height: 49px; width: 270px; }
  .doc-icon { flex: none; margin-top: 3px; }

  .divider { position: absolute; left: 809px; top: 244px; width: 1px; height: 849px; background: var(--line); }

  /* Sidebar */
  .sidebar { position: absolute; left: 864px; top: 240px; width: 224px; }
  .widget-title { font-size: 16.5px; font-weight: normal; color: var(--navy); padding-bottom: 10px; border-bottom: 3px solid var(--line); position: relative; }
  .widget-title::after { content: ""; position: absolute; left: 0; bottom: -3px; width: 57px; height: 3px; background: var(--coral); }
  .cat-list { margin-top: 16px; }
  .cat-list li { display: flex; align-items: center; gap: 9px; height: 31px; font-size: 13px; }
  .badge { width: 22px; height: 22px; border-radius: 50%; background: var(--coral); color: var(--white); font-size: 12px; display: flex; align-items: center; justify-content: center; }
  .popular { margin-top: 26px; }
  .popular-list { margin-top: 18px; }
  .popular-list li { display: flex; gap: 8px; font-size: 13px; line-height: 19px; height: 48px; }

  /* Footer */
  .site-footer {
    position: absolute; left: 0; bottom: 0; width: 1200px; height: 43px;
    background: var(--footer-bg); border-top: 1px solid #e2e2e2;
    display: flex; align-items: center; justify-content: space-between; padding: 0 111px;
    font-size: 13px; color: var(--muted);
  }
  .footer-links { display: flex; gap: 10px; }
</style>
</head>
<body>
<svg width="0" height="0" style="position:absolute">
  <defs>
    <symbol id="doc" viewBox="0 0 12 14">
      <path d="M1 .8h7l3 3v9.4H1z" fill="none" stroke="#8c9096" stroke-width="1"/>
      <path d="M3 5.5h6M3 7.8h6M3 10.1h6" stroke="#8c9096" stroke-width="1"/>
    </symbol>
    <symbol id="folder" viewBox="0 0 22 17">
      <path d="M1 2h6l2 2h11v2H4.5L1 15z" fill="none" stroke="#f98065" stroke-width="1.2"/>
      <path d="M4.5 6H21l-3.5 9.5H1z" fill="none" stroke="#f98065" stroke-width="1.2"/>
    </symbol>
  </defs>
</svg>

<header class="site-header">
  <a class="brand" href="#">
    <span class="brand-mark"></span>
    <span>
      <div class="brand-name">rankvale.ch</div>
      <div class="brand-tagline">Lorem ipsum dolor sit amet</div>
    </span>
  </a>
  <nav class="top-nav"><a href="#">Blog</a><a href="#">Contact</a></nav>
  <div class="social">
    <a class="social-btn" href="#" aria-label="chirpnet"></a>
    <a class="social-btn" href="#" aria-label="brivella"></a>
  </div>
</header>

<section class="search-band">
  <div class="search-form">
    <span class="search-input">Have a question? Ask or enter a search term.</span>
    <span class="search-btn">
      <svg width="14" height="14" viewBox="0 0 14 14"><circle cx="6" cy="6" r="4.5" fill="none" stroke="#fff" stroke-width="2"/><path d="M9.3 9.3L13 13" stroke="#fff" stroke-width="2" stroke-linecap="round"/></svg>
      SEARCH
    </span>
  </div>
</section>

<main class="content">
  <h1 class="section-title">Article Categories</h1>
  <div class="category-grid">
    <div class="category">
      <div class="category-head"><svg width="21" height="17"><use href="#folder"/></svg><h3>Content SEO<span class="count">(6)</span></h3></div>
      <ul class="article-list">
        <li><svg class="doc-icon" width="12" height="14"><use href="#doc"/></svg>Reference site about Lorem Ipsum used giving information</li>
        <li><svg class="doc-icon" width="12" height="14"><use href="#doc"/></svg>Reference site about Lorem Ipsum used giving information</li>
        <li><svg class="doc-icon" width="12" height="14"><use href="#doc"/></svg>Reference site about Lorem Ipsum used giving information</li>
        <li><svg class="doc-icon" width="12" height="14"><use href="#doc"/></svg>Reference site about Lorem Ipsum used giving information</li>
      </ul>
    </div>
    <div class="category">
      <div class="category-head"><svg width="21" height="17"><use href="#folder"/></svg><h3>Technical SEO<span class="count">(3)</span></h3></div>
      <ul class="article-list">
        <li><svg class="doc-icon" width="12" height="14"><use href="#doc"/></svg>Reference site about Lorem Ipsum used giving information</li>
        <li><svg class="doc-icon" width="12" height="14"><use href="#doc"/></svg>Reference site about Lorem Ipsum used giving information</li>
        <li><svg class="doc-icon" width="12" height="14"><use href="#doc"/></svg>Reference site about Lorem Ipsum used giving information</li>
        <li><svg class="doc-icon" width="12" height="14"><use href="#doc"/></svg>Reference site about Lorem Ipsum used giving information</li>
      </ul>
    </div>
    <div class="category">
      <div class="category-head"><svg width="21" height="17"><use href="#folder"/></svg><h3>Link Building<span class="count">(6)</span></h3></div>
      <ul class="article-list">
        <li><svg class="doc-icon" width="12" height="14"><use href="#doc"/></svg>Reference site about Lorem Ipsum used giving information</li>
        <li><svg class="doc-icon" width="12" height="14"><use href="#doc"/></svg>Reference site about Lorem Ipsum used giving information</li>
        <li><svg class="doc-icon" width="12" height="14"><use href="#doc"/></svg>Reference site about Lorem Ipsum used giving information</li>
        <li><svg class="doc-icon" width="12" height="14"><use href="#doc"/></svg>Reference site about Lorem Ipsum used giving information</li>
      </ul>
    </div>
    <div class="category">
      <div class="category-head"><svg width="21" height="17"><use href="#folder"/></svg><h3>Influencer Marketing<span class="count">(4)</span></h3></div>
      <ul class="article-list">
        <li><svg class="doc-icon" width="12" height="14"><use href="#doc"/></svg>Reference site about Lorem Ipsum used giving information</li>
        <li><svg class="doc-icon" width="12" height="14"><use href="#doc"/></svg>Reference site about Lorem Ipsum used giving information</li>
        <li><svg class="doc-icon" width="12" height="14"><use href="#doc"/></svg>Reference site about Lorem Ipsum used giving information</li>
        <li><svg class="doc-icon" width="12" height="14"><use href="#doc"/></svg>Reference site about Lorem Ipsum used giving information</li>
      </ul>
    </div>
    <div class="category">
      <div class="category-head"><svg width="21" height="17"><use href="#folder"/></svg><h3>Paid Marketing<span class="count">(5)</span></h3></div>
      <ul class="article-list">
        <li><svg class="doc-icon" width="12" height="14"><use href="#doc"/></svg>Reference site about Lorem Ipsum used giving information</li>
        <li><svg class="doc-icon" width="12" height="14"><use href="#doc"/></svg>Reference site about Lorem Ipsum used giving information</li>
        <li><svg class="doc-icon" width="12" height="14"><use href="#doc"/></svg>Reference site about Lorem Ipsum used giving information</li>
        <li><svg class="doc-icon" width="12" height="14"><use href="#doc"/></svg>Reference site about Lorem Ipsum used giving information</li>
      </ul>
    </div>
    <div class="category">
      <div class="category-head"><svg width="21" height="17"><use href="#folder"/></svg><h3>Analytics &amp; Measurement<span class="count">(4)</span></h3></div>
      <ul class="article-list">
        <li><svg class="doc-icon" width="12" height="14"><use href="#doc"/></svg>Reference site about Lorem Ipsum used giving information</li>
        <li><svg class="doc-icon" width="12" height="14"><use href="#doc"/></svg>Reference site about Lorem Ipsum used giving information</li>
        <li><svg class="doc-icon" width="12" height="14"><use href="#doc"/></svg>Reference site about Lorem Ipsum used giving information</li>
        <li><svg class="doc-icon" width="12" height="14"><use href="#doc"/></svg>Reference site about Lorem Ipsum used giving information</li>
      </ul>
    </div>
  </div>
</main>

<div class="divider"></div>

<aside class="sidebar">
  <h2 class="widget-title">Categories</h2>
  <ul class="cat-list">
    <li><span class="badge">6</span>Content SEO</li>
    <li><span class="badge">3</span>Technical SEO</li>
    <li><span class="badge">6</span>Link Building</li>
    <li><span class="badge">4</span>Influencer Marketing</li>
    <li><span class="badge">5</span>Paid Marketing</li>
    <li><span class="badge">4</span>Analytics &amp; Measurement</li>
  </ul>

  <div class="popular">
    <h2 class="widget-title">Popular Articles</h2>
    <ul class="popular-list">
      <li><svg class="doc-icon" width="12" height="14"><use href="#doc"/></svg>Reference site about Lorem Ipsum, giving information</li>
      <li><svg class="doc-icon" width="12" height="14"><use href="#doc"/></svg>Reference site about Lorem Ipsum, giving information</li>
      <li><svg class="doc-icon" width="12" height="14"><use href="#doc"/></svg>Reference site about Lorem Ipsum, giving information</li>
      <li><svg class="doc-icon" width="12" height="14"><use href="#doc"/></svg>Reference site about Lorem Ipsum, giving information</li>
      <li><svg class="doc-icon" width="12" height="14"><use href="#doc"/></svg>Reference site about Lorem Ipsum, giving information</li>
    </ul>
  </div>

  <div class="popular" style="margin-top:22px">
    <h2 class="widget-title">Popular Articles</h2>
    <ul class="popular-list">
      <li><svg class="doc-icon" width="12" height="14"><use href="#doc"/></svg>Reference site about Lorem Ipsum, giving information</li>
      <li><svg class="doc-icon" width="12" height="14"><use href="#doc"/></svg>Reference site about Lorem Ipsum, giving information</li>
      <li><svg class="doc-icon" width="12" height="14"><use href="#doc"/></svg>Reference site about Lorem Ipsum, giving information</li>
      <li><svg class="doc-icon" width="12" height="14"><use href="#doc"/></svg>Reference site about Lorem Ipsum, giving information</li>
      <li><svg class="doc-icon" width="12" height="14"><use href="#doc"/></svg>Reference site about Lorem Ipsum, giving information</li>
    </ul>
  </div>
</aside>

<footer class="site-footer">
  <span>Copyright 2017 All Rights Reserved.</span>
  <nav class="footer-links"><a href="#">Terms of Use</a><a href="#">Privacy</a><a href="#">Sitemap</a></nav>
</footer>
</body>
</html>
```